Webdesign für Gebäudereinigung
Zielgruppe
Seit 2005 ist LUM Dienstleistungen der Partner für Gebäudereinigung in Berlin. Wir haben Firmenkunden sowie privat Kunden und kümmern uns um sämtliche Reinigungen. Wie Glasreinigung, Büro- und Unterhaltungsreinigung, Bau- und Baufeinreinigung, Aufgangsreinigung & Grundreinigung…
Aufgabenstellung
Unsere neue Webseite sollte modern - Zeitlos - freundlich sein … Farben am Logo orientieren, das übernehmen wir weiterhin….

```html
<!DOCTYPE html>
<html lang="de">
<head>
<meta charset="utf-8">
<title>LUM Dienstleistungen – Gebäudereinigung Berlin</title>
<link href="https://fonts.googleapis.com/css2?family=Roboto:wght@400;500;700&display=swap" rel="stylesheet">
<style>
:root{
  --orange:#f26a1b;
  --ink:#222428;
  --text:#55585e;
  --muted:#8a8d92;
  --navy:#2c3e6b;
  --light:#f4f5f7;
  --line:#e4e6ea;
  --dark:#333437;
  --white:#ffffff;
}
*{box-sizing:border-box;margin:0;padding:0}
html,body{width:1200px;height:4540px;overflow:hidden}
body{font-family:"Roboto",Arial,sans-serif;color:var(--ink);background:var(--white);position:relative}
.abs{position:absolute}
.section{position:absolute;left:0;width:1200px}
.label{color:var(--orange);font-size:12px;font-weight:500}
.h2{font-size:24px;font-weight:700;line-height:1.3;color:var(--ink)}
.center{text-align:center;left:0;width:1200px}
.btn{position:absolute;background:var(--orange);color:var(--white);font-size:11px;font-weight:500;display:flex;align-items:center;justify-content:center;border-radius:3px}
.photo{position:absolute}
.logo{position:absolute;display:flex;align-items:flex-end;gap:8px}
.logo-square{width:56px;height:67px;background:var(--navy)}
.logo-name{font-size:13px;font-weight:500;color:var(--navy);padding-bottom:6px}
.nav a{position:absolute;top:41px;font-size:12px;color:var(--ink);text-decoration:none}
.check{position:absolute;display:flex;align-items:center;gap:10px;font-size:12px;font-weight:500}
.check i{width:16px;height:16px;border-radius:50%;background:var(--ink);display:inline-flex;align-items:center;justify-content:center}
.card{position:absolute;background:var(--white);box-shadow:0 2px 10px rgba(0,0,0,.05)}
.dots{position:absolute;display:flex;gap:6px;justify-content:center;left:0;width:1200px}
.dots span{width:22px;height:3px;background:var(--muted)}
.dots span.on{background:var(--orange)}
.badge{position:absolute;top:502px;width:116px;height:40px;background:var(--white);box-shadow:0 2px 8px rgba(0,0,0,.08);display:flex;align-items:center;justify-content:center}
.badge b{width:70px;height:14px;background:#d7dbe3;border-radius:2px}
.review p{font-size:11.5px;line-height:1.62;color:var(--text)}
.arrow{position:absolute;width:24px;height:24px}
.footer{background:var(--dark);color:#d9dadc}
.footer h4{font-size:14px;font-weight:500;color:var(--white)}
.footer p,.footer li{font-size:11.5px;line-height:1.65}
.footer ul{list-style:none}
.footer li::before{content:"• ";color:var(--orange)}
</style>
</head>
<body>

<!-- Hero -->
<section class="section" style="top:0;height:485px;background:linear-gradient(90deg,#fbfbfc 0%,#f5f6f8 55%,#e3e7ec 75%,#d9dee5 100%)">
  <div class="photo" role="img" aria-label="Helle, moderne Empfangshalle mit großen Glasfronten" style="left:700px;top:0;width:500px;height:485px;background:linear-gradient(90deg,rgba(250,251,252,1) 0%,rgba(225,230,236,.6) 40%,#cfd6de 100%)"></div>
  <div class="logo" style="left:162px;top:0">
    <div class="logo-square"></div><div class="logo-name">LUM Dienstleistungen</div>
  </div>
  <nav class="nav">
    <a style="left:554px">Über uns</a>
    <a style="left:641px">Referenzen</a>
    <a style="left:737px">Leistungen</a>
    <a style="left:836px;color:var(--orange);font-weight:500;display:flex;gap:6px;align-items:center;top:39px">
      <svg width="14" height="14" viewBox="0 0 24 24"><path fill="#f26a1b" d="M6.6 10.8a15 15 0 0 0 6.6 6.6l2.2-2.2a1 1 0 0 1 1-.25 11.4 11.4 0 0 0 3.6.57 1 1 0 0 1 1 1V20a1 1 0 0 1-1 1A17 17 0 0 1 3 4a1 1 0 0 1 1-1h3.5a1 1 0 0 1 1 1c0 1.25.2 2.45.57 3.6a1 1 0 0 1-.25 1z"/></svg>030 - 512 604 37</a>
  </nav>
  <div class="btn" style="left:965px;top:31px;width:73px;height:37px">Kontakt</div>
  <h1 class="abs" style="left:162px;top:145px;font-size:37px;font-weight:700;line-height:1.27">Ihr kompetenter Partner<br>für die Objektreinigung</h1>
  <p class="abs" style="left:162px;top:256px;font-size:15px;line-height:1.55;color:var(--text)">Seit 2005 überzeugt L.U.M. Gebäudereinigung aus Berlin durch<br>fachliches Know-how und hoher Motivation. Überzeugen Sie sich.</p>
  <div class="btn" style="left:162px;top:338px;width:152px;height:37px">Unsere Leistungen</div>
  <div class="abs" style="left:345px;top:334px;width:60px;height:48px;border-radius:50%;background:#3c3e44"></div>
</section>

<!-- Partner badges -->
<section class="section" style="top:485px;height:75px;background:var(--light)"></section>
<div class="badge" style="left:162px"><b></b></div>
<div class="badge" style="left:328px"><b></b></div>
<div class="badge" style="left:495px"><b></b></div>
<div class="badge" style="left:661px"><b></b></div>
<div class="badge" style="left:828px"><b></b></div>

<!-- About -->
<section class="section" style="top:560px;height:601px">
  <div class="photo" role="img" aria-label="Reinigungskraft beim Putzen einer Glasfassade" style="left:0;top:74px;width:485px;height:328px;background:linear-gradient(135deg,#b9cfe6,#7fa6cf 55%,#3d4b5e)"></div>
  <div class="photo" role="img" aria-label="Team in blauen Poloshirts mit Reinigungsutensilien" style="left:226px;top:322px;width:331px;height:216px;border:8px solid var(--white);background:linear-gradient(160deg,#e9edf2,#9fb3d6 50%,#3463b5)"></div>
  <div class="abs label" style="left:604px;top:94px">Über uns ipsum dolor sit amet.</div>
  <h2 class="abs h2" style="left:604px;top:120px">L.U.M. Gebäudereinigung in Berlin -<br>beste Qualität und hohe Motivation</h2>
  <p class="abs" style="left:604px;top:214px;width:420px;font-size:13.5px;line-height:1.75;color:var(--text)">L.U.M. Gebäudereinigung in Berlin existiert bereits seit 2005 und ist Mitglied der Industrie- und Handelskammer (IHK). Unser Team besticht durch fachliches Know-how und eine hohe Motivation. Was uns auszeichnet sind Flexibilität, Zuverlässigkeit und Gründlichkeit.</p>
</section>
<svg width="0" height="0" style="position:absolute"><defs><symbol id="arr" viewBox="0 0 16 16"><circle cx="8" cy="8" r="8" fill="#222428"/><path d="M5 8h6M8.5 5.5 11 8l-2.5 2.5" stroke="#fff" stroke-width="1.5" fill="none"/></symbol></defs></svg>
<div class="check" style="left:604px;top:927px"><svg width="16" height="16"><use href="#arr"/></svg>15+ Jahre Erfahrung</div>
<div class="check" style="left:604px;top:957px"><svg width="16" height="16"><use href="#arr"/></svg>20+ MitarbeiterInnen</div>
<div class="check" style="left:604px;top:988px"><svg width="16" height="16"><use href="#arr"/></svg>Mitglied IHK</div>
<div class="check" style="left:826px;top:927px"><svg width="16" height="16"><use href="#arr"/></svg>Meisterliches Fachwissen</div>
<div class="check" style="left:826px;top:957px"><svg width="16" height="16"><use href="#arr"/></svg>Hohe Motivation</div>
<div class="check" style="left:826px;top:988px"><svg width="16" height="16"><use href="#arr"/></svg>Gründlich und sauber</div>
<div class="btn" style="left:604px;top:1045px;width:185px;height:37px">Erfahren Sie mehr zu uns</div>

<!-- Services -->
<section class="section" style="top:1161px;height:612px;background:linear-gradient(90deg,#e6e7ea 0%,#f3f4f6 25%,#f6f7f8 100%)">
  <div class="photo" role="img" aria-label="Reinigungsmaschine auf hellem Boden, blass im Hintergrund" style="left:0;top:0;width:200px;height:612px;background:linear-gradient(90deg,rgba(200,150,140,.25),rgba(240,241,243,0))"></div>
  <div class="abs label center" style="top:71px">Profitieren auch Sie von unseren Leistungen</div>
  <h2 class="abs h2 center" style="top:99px">Beratung und Information</h2>
</section>
<svg class="arrow" style="left:108px;top:1473px" viewBox="0 0 24 24"><path d="M15 4 7 12l8 8" stroke="#555" stroke-width="1.8" fill="none"/></svg>
<svg class="arrow" style="left:1068px;top:1473px" viewBox="0 0 24 24"><path d="M9 4l8 8-8 8" stroke="#555" stroke-width="1.8" fill="none"/></svg>
<div class="card" style="left:162px;top:1371px;width:275px;height:229px">
  <svg class="abs" style="left:34px;top:26px" width="36" height="44" viewBox="0 0 24 30"><path d="M12 2c1 5 7 8 7 15a7 7 0 0 1-14 0c0-4 2-6 3-8 0 3 1 4 2 5 0-5 2-8 2-12z" stroke="#f26a1b" stroke-width="1.6" fill="none"/><path d="M12 18c1 2 3 3 3 5a3 3 0 0 1-6 0c0-2 2-3 3-5z" stroke="#f26a1b" stroke-width="1.4" fill="none"/></svg>
  <div class="abs" style="left:35px;top:106px;font-size:16px;font-weight:500">Aufgangsreinigung</div>
  <div class="abs" style="left:35px;top:153px;width:205px;height:1px;background:var(--line)"></div>
  <div class="check" style="left:35px;top:178px;font-size:11.5px"><svg width="16" height="16"><use href="#arr"/></svg>Mehr Infos</div>
</div>
<div class="card" style="left:462px;top:1371px;width:275px;height:229px">
  <svg class="abs" style="left:34px;top:26px" width="36" height="44" viewBox="0 0 24 30"><path d="M12 2c1 5 7 8 7 15a7 7 0 0 1-14 0c0-4 2-6 3-8 0 3 1 4 2 5 0-5 2-8 2-12z" stroke="#f26a1b" stroke-width="1.6" fill="none"/><path d="M12 18c1 2 3 3 3 5a3 3 0 0 1-6 0c0-2 2-3 3-5z" stroke="#f26a1b" stroke-width="1.4" fill="none"/></svg>
  <div class="abs" style="left:35px;top:106px;font-size:16px;font-weight:500">Baureinigung</div>
  <div class="abs" style="left:35px;top:153px;width:205px;height:1px;background:var(--line)"></div>
  <div class="check" style="left:35px;top:178px;font-size:11.5px"><svg width="16" height="16"><use href="#arr"/></svg>Mehr Infos</div>
</div>
<div class="card" style="left:762px;top:1371px;width:276px;height:229px">
  <svg class="abs" style="left:34px;top:26px" width="36" height="44" viewBox="0 0 24 30"><path d="M12 2c1 5 7 8 7 15a7 7 0 0 1-14 0c0-4 2-6 3-8 0 3 1 4 2 5 0-5 2-8 2-12z" stroke="#f26a1b" stroke-width="1.6" fill="none"/><path d="M12 18c1 2 3 3 3 5a3 3 0 0 1-6 0c0-2 2-3 3-5z" stroke="#f26a1b" stroke-width="1.4" fill="none"/></svg>
  <div class="abs" style="left:35px;top:106px;font-size:16px;font-weight:500">Büroreinigung</div>
  <div class="abs" style="left:35px;top:153px;width:205px;height:1px;background:var(--line)"></div>
  <div class="check" style="left:35px;top:178px;font-size:11.5px"><svg width="16" height="16"><use href="#arr"/></svg>Mehr Infos</div>
</div>
<div class="dots" style="top:1636px"><span class="on"></span><span></span></div>
<div class="btn" style="left:502px;top:1676px;width:196px;height:37px">Alle Leistungen anschauen</div>

<!-- Advantages -->
<section class="section" style="top:1773px;height:557px">
  <div class="abs label" style="left:181px;top:72px">Vorteile für den Kunden amet consetetur.</div>
  <h2 class="abs h2" style="left:181px;top:99px">Umfangreiches Angebot und<br>erstklassig ausgebildete Mitarbeiter</h2>
  <p class="abs" style="left:181px;top:182px;width:410px;font-size:13.5px;line-height:1.75;color:var(--text)">Lorem ipsum dolor sit amet, consetetur sadipscing elitr, sed diam nonumy eirmod tempor invidunt ut labore et dolore magna aliquyam erat, sed diam voluptua. At vero eos et accusam et justo duo dolores et ea rebum. Stet clita kasd gubergren, no sea takimata sanctus est Lorem ipsum dolor.</p>
  <div class="photo" role="img" aria-label="Teppichreinigung mit Saugdüse, frisch gereinigte Bahn im Teppich" style="left:649px;top:84px;width:354px;height:393px;background:linear-gradient(170deg,#3b4a6e 0%,#8d8f96 35%,#b3b5ba 70%,#9d9fa4 100%)"></div>
</section>
<div class="check" style="left:181px;top:2111px"><svg width="16" height="16"><use href="#arr"/></svg>At vero takimata sanctus est Lorem ipsum dolor</div>
<div class="check" style="left:181px;top:2141px"><svg width="16" height="16"><use href="#arr"/></svg>Vero takimata sanctus est Lorem ipsum dolor</div>
<div class="check" style="left:181px;top:2172px"><svg width="16" height="16"><use href="#arr"/></svg>At vero takimata sanctus est Lorem ipsum dolor</div>
<div class="btn" style="left:181px;top:2229px;width:184px;height:37px">Erfahren Sie mehr zu uns</div>

<!-- Testimonials -->
<section class="section" style="top:2330px;height:789px;background:var(--light)">
  <div class="abs label center" style="top:73px">Wir lassen unsere Kunden sprechen</div>
  <h2 class="abs h2 center" style="top:103px">Unsere Kunden liegen uns am Herzen.<br>Überzeugen Sie sich selbst.</h2>
</section>
<div class="card review" style="left:162px;top:2537px;width:275px;height:413px">
  <div class="abs" style="left:25px;top:26px;color:#f5c518;font-size:22px;letter-spacing:2px">★★★★★</div>
  <div class="abs" style="left:25px;top:82px;font-size:15.5px;font-weight:500">Top! At vero magna.</div>
  <p class="abs" style="left:25px;top:111px;width:228px">„Lorem ipsum dolor sit amet, consetetur sadipscing elitr, sed diam nonumy eirmod tempor invidunt ut labore et dolore magna aliquyam erat, sed diam voluptua. At vero eos et accusam et justo duo dolores et ea rebum. Stet clita kasd gubergren, no sea takimata sanctus est Lorem ipsum dolor sit. At vero eos et accusam et justo duo dolores et ea rebum. Stet clita kasd.</p>
  <div class="abs" style="left:25px;top:326px;width:28px;height:2px;background:var(--orange)"></div>
  <div class="abs" style="left:25px;top:343px;font-size:11.5px;line-height:1.6"><b style="font-weight:500">Sabine Kröger</b><br>aus Musterstadt</div>
</div>
<div class="card review" style="left:462px;top:2537px;width:275px;height:413px">
  <div class="abs" style="left:25px;top:26px;color:#f5c518;font-size:22px;letter-spacing:2px">★★★★★</div>
  <div class="abs" style="left:25px;top:82px;font-size:15.5px;font-weight:500">Lorem ipsum dolor sit.</div>
  <p class="abs" style="left:25px;top:111px;width:228px">„Lorem ipsum dolor sit amet, consetetur sadipscing elitr, sed diam nonumy eirmod tempor invidunt ut labore et dolore magna aliquyam erat, sed diam voluptua. At vero eos et accusam et justo duo dolores et ea rebum. Stet clita kasd gubergren, no sea takimata sanctus est Lorem ipsum dolor sit.</p>
  <div class="abs" style="left:25px;top:326px;width:28px;height:2px;background:var(--orange)"></div>
  <div class="abs" style="left:25px;top:343px;font-size:11.5px;line-height:1.6"><b style="font-weight:500">Max Muster</b><br>aus Musterstadt</div>
</div>
<div class="card review" style="left:762px;top:2537px;width:276px;height:413px">
  <div class="abs" style="left:25px;top:26px;color:#f5c518;font-size:22px;letter-spacing:2px">★★★★★</div>
  <div class="abs" style="left:25px;top:82px;font-size:15.5px;font-weight:500">Tolles Team. Vielen Dank!</div>
  <p class="abs" style="left:25px;top:111px;width:228px">„Lorem ipsum dolor sit amet, consetetur sadipscing elitr, sed diam nonumy eirmod tempor invidunt ut labore et dolore magna aliquyam erat, sed diam voluptua. At vero eos et accusam et justo duo dolores et ea rebum. Stet clita kasd gubergren, no sea takimata sanctus est Lorem ipsum dolor sit. At vero eos et accusam et justo duo.</p>
  <div class="abs" style="left:25px;top:326px;width:28px;height:2px;background:var(--orange)"></div>
  <div class="abs" style="left:25px;top:343px;font-size:11.5px;line-height:1.6"><b style="font-weight:500">Maximilian Mustermann</b><br>aus Musterstadt</div>
</div>
<div class="dots" style="top:2980px"><span class="on"></span><span></span></div>
<div class="btn" style="left:488px;top:3020px;width:224px;height:37px">Alle Kundenstimmen anschauen</div>

<!-- References -->
<section class="section" style="top:3119px;height:740px">
  <div class="abs label center" style="top:79px">Aktuelle Referenzen</div>
  <h2 class="abs h2 center" style="top:111px">Erfolgreiche Zusammenarbeit<br>mit zufriedenen Kunden</h2>
  <div class="photo" role="img" aria-label="Treppenhaus mit Geländer in einem Bürogebäude" style="left:0;top:206px;width:275px;height:349px;background:linear-gradient(135deg,#d8dbe6,#a7adc8 50%,#c9b89a)"></div>
  <div class="photo" role="img" aria-label="Hand wischt mit Tuch über einen Schreibtisch im Büro" style="left:337px;top:206px;width:525px;height:349px;background:linear-gradient(160deg,#eef0f1 0%,#c8cdd0 45%,#3f4346 100%)"></div>
  <div class="abs" style="left:362px;top:470px;width:22px;height:2px;background:var(--orange)"></div>
  <div class="abs" style="left:362px;top:477px;font-size:17px;font-weight:500;color:var(--white)">Reinigung Referenz</div>
  <div class="abs" style="left:362px;top:504px;font-size:11.5px;color:#e8e8e8">Zusatzinfo zur Referenz</div>
  <div class="photo" role="img" aria-label="Helles Großraumbüro mit Glaswänden" style="left:925px;top:206px;width:275px;height:349px;background:linear-gradient(135deg,#eef1f4,#c9d3dc 60%,#dfe5ea)"></div>
</section>
<svg class="arrow" style="left:294px;top:3486px" viewBox="0 0 24 24"><path d="M15 4 7 12l8 8" stroke="#555" stroke-width="1.8" fill="none"/></svg>
<svg class="arrow" style="left:881px;top:3486px" viewBox="0 0 24 24"><path d="M9 4l8 8-8 8" stroke="#555" stroke-width="1.8" fill="none"/></svg>
<div class="dots" style="top:3709px"><span class="on"></span><span></span><span></span><span></span></div>
<div class="btn" style="left:502px;top:3760px;width:196px;height:37px">Alle Referenzen anschauen</div>

<!-- Contact CTA -->
<section class="section" style="top:3859px;height:264px;background:var(--light)">
  <div class="abs label center" style="top:70px">Jetzt kostenlose Erstberatung vereinbaren</div>
  <h2 class="abs h2 center" style="top:101px">Haben Sie Fragen und suchen Beratung?<br>Nehmen Sie Kontakt mit uns auf:</h2>
  <div class="abs" style="left:0;width:1200px;top:175px;display:flex;justify-content:center;align-items:center;gap:10px;color:var(--orange);font-size:30px;font-weight:500">
    <svg width="26" height="26" viewBox="0 0 24 24"><path fill="#f26a1b" d="M6.6 10.8a15 15 0 0 0 6.6 6.6l2.2-2.2a1 1 0 0 1 1-.25 11.4 11.4 0 0 0 3.6.57 1 1 0 0 1 1 1V20a1 1 0 0 1-1 1A17 17 0 0 1 3 4a1 1 0 0 1 1-1h3.5a1 1 0 0 1 1 1c0 1.25.2 2.45.57 3.6a1 1 0 0 1-.25 1z"/></svg>030 - 512 604 37
  </div>
</section>

<!-- Footer -->
<footer class="section footer" style="top:4123px;height:417px">
  <div class="logo" style="left:162px;top:39px">
    <div class="logo-square" style="height:63px"></div><div class="logo-name" style="color:var(--white)">LUM Dienstleistungen</div>
  </div>
  <div class="abs" style="left:657px;top:75px;font-size:14px;font-weight:500;color:var(--white)">Jetzt unverbindlich anfragen!</div>
  <div class="btn" style="left:885px;top:64px;width:153px;height:37px">Angebot anfordern</div>
  <p class="abs" style="left:162px;top:167px;width:360px">Kurzer Beschreibungstext zum Unternehmen, Leistungen und Services ipsum dolor sit amet, consetetur sadipscing elitr, sed diam nonumy eirmod tempor invidunt ut labore et dolore magna aliquyam erat, sed diam voluptua. At vero eos et accusam et justo duo dolores et ea rebum. Stet clita kasd gubergren, no sea takimata sanctus est Lorem ipsum dolor sit amet. Lorem ipsum dolor sit amet, consetetur sadipscing elitr, sed diam nonumy eirmod tempor invidunt ut labore et ... <span style="color:var(--orange);text-decoration:underline">Jetzt mehr erfahren</span></p>
  <h4 class="abs" style="left:629px;top:168px">Anschrift &amp; Kontakt</h4>
  <p class="abs" style="left:629px;top:204px"><b style="font-weight:500;color:var(--white)">L.U.M. Dienstleistungen</b><br>Lindenhofweg 14<br>10629 Berlin<br><br>030 512 604 37<br>info@gebaeudereinigung-lum.de</p>
  <h4 class="abs" style="left:920px;top:168px">Wichtige Links</h4>
  <ul class="abs" style="left:920px;top:204px;line-height:2"><li>Über uns</li><li>Referenzen</li><li>Leistungen</li><li>Kontakt</li></ul>
  <div class="abs" style="left:162px;top:383px;font-size:11.5px">© 2022 LUM Gebäudereinigung für Berlin</div>
  <div class="abs" style="left:849px;top:383px;font-size:11.5px;display:flex;gap:20px"><span>AGB</span><span>Datenschutz</span><span>Impressum</span></div>
</footer>

</body>
</html>
```